Single brochure for international companies in the financial sector

We need to update a brochure 4 pages presenting our company. We are a financial engineering company. The final design must provide financial security, service and trust. you will find the current brochure copy. Our color code is Orange (RGB 235/100/68), Black, White and Gray. photos show the visual of the site, but it is not mandatory to keep them.

Target Market(s)

wealth management professionals

Industry/Entity Type

Finance

Requirements
Must have
• Logo Tolvane Capital all text in the document color Orange Tolvane (RGB 235/100/68)
Nice to have
• Vista Font
Should not have
• images / pictures of people

```html
<!DOCTYPE html>
<html lang="en">
<head>
<meta charset="utf-8">
<title>Tolvane Capital — Financial Engineering brochure covers</title>
<link rel="stylesheet" href="https://fonts.googleapis.com/css2?family=Questrial&display=swap">
<style>
  :root {
    --orange: #eb6444;
    --orange-deep: #d9573a;
    --charcoal: #333333;
    --white: #ffffff;
    --paper-grey: #e9e9e9;
    --backdrop: #e4e4e4;
    --sky-light: #dde6f0;
    --sky-mid: #9fb3cc;
    --glass: #4a5f7c;
    --icon-dark: #6b3426;
  }
  * { box-sizing: border-box; margin: 0; padding: 0; }
  html, body {
    width: 874px; height: 1200px; overflow: hidden;
    background: var(--backdrop);
    font-family: "Questrial", "Century Gothic", sans-serif;
  }
  .canvas { position: relative; width: 874px; height: 1200px; }

  .cover {
    position: absolute; left: 247px; width: 380px; height: 520px;
    overflow: hidden; box-shadow: 6px 10px 24px rgba(0,0,0,.18);
  }
  .cover--front { top: 45px; background: linear-gradient(120deg, var(--paper-grey) 0%, var(--white) 55%); }
  .cover--back { top: 635px; background: var(--orange); }

  /* Front cover */
  .brand {
    position: absolute; left: 0; right: 0; text-align: center;
    color: var(--orange); line-height: 1;
  }
  .brand__name { display: block; font-size: 15px; letter-spacing: 9px; padding-left: 9px; }
  .brand__sub { display: block; font-size: 9px; letter-spacing: 4px; padding-left: 4px; margin-top: 5px; }
  .cover--front .brand { top: 70px; }

  .cover-photo {
    position: absolute; left: 0; top: 115px; width: 380px; height: 320px;
    background:
      linear-gradient(100deg, rgba(255,255,255,.95) 0%, rgba(255,255,255,0) 35%),
      linear-gradient(200deg, var(--glass) 0%, var(--sky-mid) 45%, var(--sky-light) 100%);
    clip-path: polygon(0 0, 100% 0, 100% 72%, 0 96%);
  }
  .cover-band { position: absolute; left: 0; top: 0; }

  .cover-title {
    position: absolute; left: 0; right: 0; top: 400px; text-align: center;
    color: var(--white); font-size: 29px; line-height: 1.15; letter-spacing: .5px;
    font-weight: 400;
  }
  .cover-url {
    position: absolute; left: 0; right: 0; bottom: 24px; text-align: center;
    color: var(--orange); font-size: 8px; letter-spacing: 3px;
  }

  /* Back cover */
  .back-photo {
    position: absolute; left: 20px; top: 30px; width: 360px; height: 420px;
    background: radial-gradient(ellipse at 40% 45%, var(--orange-deep) 0%, rgba(217,87,58,.5) 45%, rgba(235,100,68,0) 75%);
  }
  .cover--back .brand { top: 185px; color: var(--white); }
  .cover--back .brand__name { font-size: 12px; letter-spacing: 7px; padding-left: 7px; }
  .cover--back .brand__sub { font-size: 8px; }

  .contact {
    position: absolute; left: 0; right: 0; top: 225px; text-align: center;
    color: var(--white); font-size: 7.5px; line-height: 1.35; list-style: none;
  }
  .contact__item { margin-bottom: 5px; }
  .contact__bank { font-weight: 700; margin-bottom: 6px; }
  .contact__icon { display: block; margin: 0 auto 3px; width: 8px; height: 8px; }
  .cover--back .cover-url { color: var(--white); bottom: 34px; }
</style>
</head>
<body>
<main class="canvas">

  <section class="cover cover--front" aria-label="Front cover">
    <div class="cover-photo" role="img" aria-label="Photograph of glass office towers seen from below against a pale sky"></div>
    <svg class="cover-band" width="380" height="520" viewBox="0 0 380 520" aria-hidden="true">
      <polygon points="0,424 380,345 380,520 0,520" fill="var(--charcoal)"/>
      <line x1="0" y1="424" x2="380" y2="345" stroke="var(--white)" stroke-width="2"/>
    </svg>
    <div class="brand">
      <span class="brand__name">TOLVANE</span>
      <span class="brand__sub">CAPITAL</span>
    </div>
    <h1 class="cover-title">FINANCIAL<br>ENGINEERING</h1>
    <p class="cover-url">www.tolvanecapital.com</p>
  </section>

  <section class="cover cover--back" aria-label="Back cover">
    <div class="back-photo" role="img" aria-label="Faint tinted photograph of the Eiffel Tower"></div>
    <div class="brand">
      <span class="brand__name">TOLVANE</span>
      <span class="brand__sub">CAPITAL</span>
    </div>
    <ul class="contact">
      <li class="contact__item contact__bank">CODE BANQUE (CIB) : 14270</li>
      <li class="contact__item">
        <svg class="contact__icon" viewBox="0 0 10 10" aria-hidden="true"><path d="M5 0.5a3.2 3.2 0 0 0-3.2 3.2C1.8 6 5 9.5 5 9.5s3.2-3.5 3.2-5.8A3.2 3.2 0 0 0 5 .5zm0 4.5a1.3 1.3 0 1 1 0-2.6 1.3 1.3 0 0 1 0 2.6z" fill="var(--icon-dark)"/></svg>
        Tolvane Capital SA, Capital :<br>400 000 Euros<br>RCS Paris : 812 446 503
      </li>
      <li class="contact__item">
        <svg class="contact__icon" viewBox="0 0 10 10" aria-hidden="true"><path d="M2.2 .8l1.5 1.8-.9 1.2c.6 1.3 1.6 2.3 2.9 2.9l1.2-.9 1.8 1.5-.9 1.6C4.6 8.9 1.1 5.4.6 1.7z" fill="var(--icon-dark)"/></svg>
        +33 1 48 20 61 75
      </li>
      <li class="contact__item">
        <svg class="contact__icon" viewBox="0 0 10 10" aria-hidden="true"><rect x=".8" y="2" width="8.4" height="6" fill="var(--icon-dark)"/><path d="M.8 2L5 5.5 9.2 2" stroke="var(--orange)" stroke-width=".8" fill="none"/></svg>
        contact@tolvanecapital.com
      </li>
    </ul>
    <p class="cover-url">www.tolvanecapital.com</p>
  </section>

</main>
</body>
</html>
```